Real estate agent : RT Estates

I have done the attached logo designed by your company .
My business card description as below:
Name : Daniel Brooks
Mobile: 0412583047
Email : danielb@rtestates-demo.net.au
Sales & Property Management

```html
<!DOCTYPE html>
<html lang="en">
<head>
<meta charset="utf-8">
<title>RT Estates — Business Card</title>
<link href="https://fonts.googleapis.com/css2?family=Bebas+Neue&family=Lato:wght@400;700&display=swap" rel="stylesheet">
<style>
  :root {
    --page-bg: #c8c8c8;
    --card-bg: #000000;
    --ink: #ffffff;
  }
  * { margin: 0; padding: 0; box-sizing: border-box; }
  html, body {
    width: 1200px;
    height: 1200px;
    overflow: hidden;
    background: var(--page-bg);
  }
  .canvas {
    position: relative;
    width: 1200px;
    height: 1200px;
  }
  .card {
    position: absolute;
    left: 188px;
    width: 824px;
    height: 474px;
    background: var(--card-bg);
    color: var(--ink);
  }
  .card--front { top: 91px; }
  .card--back { top: 635px; }

  .holder-name {
    position: absolute;
    left: 79px;
    top: 202px;
    font-family: "Bebas Neue", "Oswald", sans-serif;
    font-size: 72px;
    line-height: 1;
    letter-spacing: 0.5px;
    white-space: nowrap;
  }
  .divider {
    position: absolute;
    left: 411px;
    top: 213px;
    width: 3px;
    height: 49px;
    background: var(--ink);
  }
  .contact-list {
    position: absolute;
    left: 449px;
    top: 212px;
    list-style: none;
    font-family: "Lato", sans-serif;
    font-size: 21px;
    line-height: 29px;
  }
  .contact-item {
    display: flex;
    align-items: center;
    white-space: nowrap;
  }
  .contact-icon {
    width: 20px;
    height: 22px;
    margin-right: 9px;
    flex: none;
  }
  .services {
    position: absolute;
    left: 238px;
    top: 397px;
    font-family: "Lato", sans-serif;
    font-size: 21px;
    letter-spacing: -0.2px;
    white-space: nowrap;
  }
  .brand {
    font-family: "Lato", sans-serif;
    font-weight: 700;
    color: var(--ink);
    text-align: center;
    line-height: 1;
  }
  .brand--small {
    position: absolute;
    left: 641px;
    top: 370px;
    width: 110px;
  }
  .brand--small .brand-initials { font-size: 46px; letter-spacing: 2px; }
  .brand--small .brand-word { font-size: 18px; letter-spacing: 3px; margin-top: 6px; }
  .brand--large {
    position: absolute;
    left: 0;
    right: 0;
    top: 118px;
  }
  .brand--large .brand-initials { font-size: 150px; letter-spacing: 6px; }
  .brand--large .brand-word { font-size: 56px; letter-spacing: 10px; margin-top: 14px; }
</style>
</head>
<body>
<main class="canvas">
  <section class="card card--front" aria-label="Business card front">
    <h1 class="holder-name">Daniel Brooks</h1>
    <span class="divider"></span>
    <ul class="contact-list">
      <li class="contact-item">
        <svg class="contact-icon" viewBox="0 0 20 22" aria-hidden="true">
          <rect x="3.5" y="1" width="13" height="20" rx="2" fill="none" stroke="#fff" stroke-width="2"/>
          <line x1="8" y1="18" x2="12" y2="18" stroke="#fff" stroke-width="1.5"/>
        </svg>
        <span>0412583047</span>
      </li>
      <li class="contact-item">
        <svg class="contact-icon" viewBox="0 0 20 22" aria-hidden="true">
          <rect x="1" y="5" width="18" height="13" fill="#fff"/>
          <polyline points="1,5 10,12 19,5" fill="none" stroke="#000" stroke-width="1.6"/>
          <polyline points="1,18 8,11" fill="none" stroke="#000" stroke-width="1.4"/>
          <polyline points="19,18 12,11" fill="none" stroke="#000" stroke-width="1.4"/>
        </svg>
        <span>danielb@rtestates-demo.net.au</span>
      </li>
    </ul>
    <p class="services">SALES &amp; PROPERTY MANAGEMENT</p>
    <div class="brand brand--small">
      <div class="brand-initials">RT</div>
      <div class="brand-word">ESTATES</div>
    </div>
  </section>

  <section class="card card--back" aria-label="Business card back">
    <div class="brand brand--large">
      <div class="brand-initials">RT</div>
      <div class="brand-word">ESTATES</div>
    </div>
  </section>
</main>
</body>
</html>
```